A modern and fresh looking church website

Holy Fenwick’s is looking for a new site design for their church. The church is a part of a group of the ‘Corvane Fellowship’ Australia and needs to kind of tie into their branding within reason.
This means, we would need to use the logo colours (Blue, Gold, Red) throughout the website and the design needs to be fresh, modern, clean, and mobile-friendly. The front page must have the following as features:
• Sermons (Podcasts and Videos)
• Events
• Venue Hire (Weddings)
The website will be mainly information-based and will have a few forms. From our recent engagement with the church, I did draft up a mock-up design for them and even it looks better than their current site, it’s not giving a ‘stand out impression’ and has that out of date look.
The inner pages will be based off the front-page design so we will take care of that, we are just looking for a front-page design that is unique and has the wow factor.
The website will be coded by our in-house development team and will be coded in a WordPress format using Elementor pro.
We are looking for a couple of designers to design 1-3 mock-ups by taking our current draft and putting their spin to it.
Updates
Hi,
Due to Christmas and the client was on leave, the design selection has been delayed. It was not ideal as I knew this would happen.
I made contact with the client and just been told that the client is leaving the church and a handover is happening for the new staff member. The new staff member will present all designs to the board for selection. This is due to be completed by the first week of February 2021.
We thanks for your patients as this was not expected and we seeing if we can hurry this process up.

```html
<!DOCTYPE html>
<html lang="en">
<head>
<meta charset="utf-8">
<title>Holy Fenwick’s Corvane Fellowship Perth</title>
<link rel="stylesheet" href="https://fonts.googleapis.com/css2?family=Poppins:wght@400;500;600&family=Mulish:wght@400;600;700&display=swap">
<style>
:root{
  --blue:#004b8d;
  --blue-bright:#0b57a8;
  --gold:#a0700e;
  --red:#d0223f;
  --pink:#fde5ea;
  --ink:#222;
  --muted:#555;
  --bar:#f6f6f6;
  --wood:#3b2418;
}
*{box-sizing:border-box;margin:0;padding:0}
html,body{width:1200px;height:2398px;overflow:hidden}
body{font-family:'Mulish',sans-serif;color:var(--ink);background:#fff;position:relative}
.wrap{position:absolute;left:141px;width:917px}
a{color:inherit;text-decoration:none}

/* top bar */
.topbar{position:absolute;top:0;left:0;width:1200px;height:38px;background:var(--bar)}
.topbar .address{top:9px;font-size:14px;color:var(--blue);display:flex;align-items:center;gap:12px}
.social{display:flex;gap:6px}
.social span{width:25px;height:25px;border-radius:50%;display:block}
.s1{background:#3b5998}.s2{background:#d62976}.s3{background:#55acee}.s4{background:#e00}
.topbar .social{position:absolute;right:142px;top:7px}

/* header */
.header{position:absolute;top:38px;left:0;width:1200px;height:97px}
.brand{top:24px;display:flex;align-items:center;gap:12px}
.brand .dot{width:52px;height:52px;border-radius:50%;background:var(--blue)}
.brand .name{font-family:'Poppins',sans-serif;font-weight:600;font-size:26px;color:var(--blue);line-height:1}
.brand .name small{display:block;font-size:12px;font-weight:500;color:#555;letter-spacing:.5px;margin-top:6px}
.times{position:absolute;right:157px;top:26px;text-align:right;font-size:13.5px;line-height:18px}
.times .label{color:var(--red)}

/* nav */
.nav{position:absolute;top:135px;left:0;width:1200px;height:38px;background:var(--blue)}
.nav ul{list-style:none;position:absolute;left:141px;width:903px;height:38px;display:flex;justify-content:space-between;align-items:center}
.nav li{font-family:'Poppins',sans-serif;font-size:15.5px;color:#fff;height:38px;line-height:38px;padding:0 20px}
.nav li.active{background:var(--gold)}

/* hero */
.hero{position:absolute;top:173px;left:0;width:1200px;height:523px;background:linear-gradient(90deg,#6b5a4a 0%,#b9a58f 35%,#8d8a95 55%,#7a4d3a 75%,#5d6f8a 100%)}

/* notice */
.notice{position:absolute;top:696px;left:0;width:1200px;height:125px;background:var(--pink)}
.notice .icon{position:absolute;left:151px;top:28px}
.notice .rule{position:absolute;left:241px;top:25px;width:1px;height:74px;background:#c9b7bb}
.notice .text{position:absolute;left:267px;top:26px;width:780px}
.notice h2{font-family:'Poppins',sans-serif;font-weight:400;font-size:17.5px;color:#333;margin-bottom:6px}
.notice p{font-size:12.5px;line-height:23px;color:#444}

/* welcome */
.welcome{position:absolute;top:895px;left:141px;width:917px;text-align:center}
.welcome h1{font-family:'Poppins',sans-serif;font-weight:500;font-size:34px;color:var(--blue)}
.welcome .underline{width:72px;height:2px;background:var(--gold);margin:8px auto 20px}
.welcome .lead{color:var(--red);font-size:15.5px;margin-bottom:8px}
.welcome p{font-size:14.5px;line-height:25.5px;color:#222;margin-bottom:6px}
.btn{display:inline-block;margin-top:15px;background:var(--gold);color:#fff;font-size:14.5px;width:124px;height:35px;line-height:35px}

/* features */
.features{position:absolute;top:1256px;left:141px;width:917px;display:flex;justify-content:space-between}
.card{width:281px;height:277px;background:#fff;box-shadow:0 2px 8px rgba(0,0,0,.1);text-align:center}
.card .media{height:198px}
.card h3{font-family:'Poppins',sans-serif;font-weight:500;font-size:20px;line-height:24px;color:var(--blue);margin-top:14px}
.m1{background:linear-gradient(135deg,#f7dfc9,#c9b49f 60%,#3a3a3a)}
.m2{background:linear-gradient(135deg,#6d6560,#3d3836 60%,#8a7a70)}
.m3{background:linear-gradient(90deg,#e9e9ec,#bfc0c5 50%,#f3f3f5)}

/* location */
.location{position:absolute;top:1618px;left:0;width:1200px;height:458px;background:radial-gradient(ellipse at 55% 30%,#6a4a36 0%,#3b2418 55%,#24150d 100%)}
.info{position:absolute;left:141px;top:40px;color:#fff}
.info h2{font-family:'Poppins',sans-serif;font-weight:500;font-size:20px;margin-bottom:12px}
.info .row{display:flex;align-items:center;gap:12px;font-size:14.5px;height:36px}
.info .block{margin-top:26px}
.info .block h2{margin-bottom:2px}
.info .block p{font-size:14.5px;line-height:20px}
.map{position:absolute;left:607px;top:38px;width:451px;height:338px;border:3px solid var(--red);background:linear-gradient(135deg,#eceae4,#e2e4e6 50%,#f1efe6)}

/* footer */
.footer{position:absolute;top:2076px;left:0;width:1200px;height:322px;background:var(--blue-bright);color:#fff}
.footer .logo{position:absolute;left:0;width:1200px;top:58px;display:flex;justify-content:center;align-items:center;gap:14px;font-family:'Poppins',sans-serif;font-weight:600;font-size:24px}
.footer .logo .dot{width:60px;height:60px;border-radius:50%;background:#fff}
.footer ul{list-style:none;position:absolute;left:205px;width:790px;top:153px;display:flex;justify-content:space-between;font-family:'Poppins',sans-serif;font-size:15.5px}
.follow{position:absolute;left:0;width:1200px;top:205px;display:flex;justify-content:center;align-items:center;gap:10px;font-family:'Poppins',sans-serif;font-size:12.5px}
.follow .social{gap:9px}
.follow .social span{width:36px;height:36px;border:2px solid #fff}
.footer .divider{position:absolute;left:141px;width:917px;top:265px;height:1px;background:rgba(255,255,255,.35)}
.copy{position:absolute;left:0;width:1200px;top:279px;text-align:center;font-family:'Poppins',sans-serif;font-size:12px}
.copy b{font-weight:500}
</style>
</head>
<body>

<div class="topbar">
  <div class="wrap address">
    <svg width="18" height="24" viewBox="0 0 18 24"><path d="M9 1C4.6 1 1.5 4.3 1.5 8.5 1.5 14 9 22.5 9 22.5S16.5 14 16.5 8.5C16.5 4.3 13.4 1 9 1z" fill="none" stroke="#004b8d" stroke-width="1.5"/><circle cx="9" cy="8.5" r="2.8" fill="none" stroke="#004b8d" stroke-width="1.5"/></svg>
    42 Marlow Street, Ashbury, WA 6012
  </div>
  <div class="social"><span class="s1"></span><span class="s2"></span><span class="s3"></span><span class="s4"></span></div>
</div>

<header class="header">
  <div class="wrap brand">
    <span class="dot"></span>
    <div class="name">HOLY FENWICK’S<small>CORVANE FELLOWSHIP PERTH</small></div>
  </div>
  <div class="times">
    <div class="label">Weekend Services</div>
    <div>Saturday 6:00pm</div>
    <div>Sunday 8:30am to 10:20am</div>
  </div>
</header>

<nav class="nav">
  <ul>
    <li class="active">Home</li><li>Sermons</li><li>About Us</li><li>Church Life</li><li>News</li><li>Wedding</li><li>Contact Us</li>
  </ul>
</nav>

<div class="hero" role="img" aria-label="Photo of smiling church members standing together inside the church"></div>

<section class="notice">
  <svg class="icon" width="62" height="56" viewBox="0 0 62 56"><path d="M31 3 L59 53 H3 Z" fill="#e11d2d" stroke="#fff" stroke-width="3" stroke-linejoin="round"/><rect x="28" y="18" width="6" height="21" rx="2" fill="#fff"/><circle cx="31" cy="45" r="3.5" fill="#fff"/></svg>
  <div class="rule"></div>
  <div class="text">
    <h2>Holy Fenwick’s Response to Covid-19</h2>
    <p>Lorem ipsum dolor sit amectetuer adipiscing elit, sed diam nonummy nibh euismod tincidunt ut laoreet dolore magna aliquam erat volutpat Ut wisi enim ad. Sed diam nonummy nibh idunt ut laoreet dolore magna aliquam.</p>
  </div>
</section>

<section class="welcome">
  <h1>Welcome to Holy Fenwick’s Corvane Fellowship Perth</h1>
  <div class="underline"></div>
  <div class="lead">Lorem ipsum dolor sit amectetuer adipiscing elit, sed diam nonummymectetuer adipiscing elit,</div>
  <p>Lorem ipsum dolor sit amectetuer adipiscing elit, sed diamng elit, sed diam nonummy nibh euis incidunt ut laoreet dolore magna aliquam erat volutpat Ut wisi en nonummy nibh euis incidunt ut laoreet dolore magna aliquam erat volutpat Ut wisi enim ad. Sed diam nonummy nibh idunt ut laoreet dolore magna aliquam.</p>
  <p>Lorem ipsum dolor sit amectetuer adipiscing elit, sed diam nonummy nibh euis incidunt ut laoreet dolore magna aliquam erat volutpat Ut wisi enim ad. Sed diam nonummy nibh idunt ut laoreet dolore magna aliquam.</p>
  <a class="btn">READ MORE</a>
</section>

<section class="features">
  <div class="card"><div class="media m1" role="img" aria-label="Headphones lying beside a phone"></div><h3>Recent podcasts<br>&amp; Videos</h3></div>
  <div class="card"><div class="media m2" role="img" aria-label="Crowd of people mingling at an event"></div><h3>Up’n’coming<br>Events</h3></div>
  <div class="card"><div class="media m3" role="img" aria-label="Church aisle decorated with white flowers for a wedding"></div><h3>Wedding<br>Venue Hire</h3></div>
</section>

<section class="location" role="img" aria-label="Church interior with wooden pews, dimmed">
  <div class="info">
    <h2>Our Location</h2>
    <div class="row"><svg width="20" height="26" viewBox="0 0 18 24"><path d="M9 1C4.6 1 1.5 4.3 1.5 8.5 1.5 14 9 22.5 9 22.5S16.5 14 16.5 8.5C16.5 4.3 13.4 1 9 1z" fill="none" stroke="#fff" stroke-width="1.4"/><circle cx="9" cy="8.5" r="2.8" fill="none" stroke="#fff" stroke-width="1.4"/></svg>42 Marlow Street, Ashbury, WA 6012</div>
    <div class="row"><svg width="22" height="22" viewBox="0 0 24 24"><path d="M5 2h4l2 5-3 2a12 12 0 0 0 7 7l2-3 5 2v4a2 2 0 0 1-2 2A19 19 0 0 1 3 4a2 2 0 0 1 2-2z" fill="none" stroke="#fff" stroke-width="1.4"/></svg>08 5550 1427</div>
    <div class="row"><svg width="22" height="20" viewBox="0 0 24 22"><rect x="1.5" y="6" width="21" height="14" fill="none" stroke="#fff" stroke-width="1.4"/><path d="M1.5 6l10.5 8 10.5-8M5 6V2h14v4" fill="none" stroke="#fff" stroke-width="1.4"/></svg>hello@holyfenwicks.org.au</div>
    <div class="block" style="margin-top:44px"><h2>Office Hours</h2><p>Tuesday, Thursday &amp; Friday 9:00am to 4:00 pm</p></div>
    <div class="block" style="margin-top:32px"><h2>Worship Services</h2><p>Saturday 6:00 pm<br>Sunday 8:30am &amp; 10:20am</p></div>
  </div>
  <div class="map" role="img" aria-label="Street map showing the church location in the city centre"></div>
</section>

<footer class="footer">
  <div class="logo"><span class="dot"></span>Corvane Fellowship</div>
  <ul><li>Home</li><li>Sermons</li><li>About Us</li><li>Church Life</li><li>News</li><li>Wedding</li><li>Contact Us</li></ul>
  <div class="follow">Follow Us On
    <div class="social"><span class="s1"></span><span class="s2"></span><span class="s3"></span><span class="s4"></span></div>
  </div>
  <div class="divider"></div>
  <div class="copy">Copyright © 2020 <b>Holy Fenwick’s Corvane Fellowship Perth.</b> All Rights Reserved.</div>
</footer>

</body>
</html>
```